Buch-/eBook-Cover für Autobiografie
Das Disign von dem Cover hat mir auf Anhieb sehr gut gefallen. Das hat gleich "ins schwarze" getroffen. Die Kommunikation war effizient und zielgerichtet
Zielgruppe
Ich bin eine Privatperson und habe im Laufe der letzten Jahre mein Autobiografie geschrieben. Besser gesagt ist es ein autobiografischer Roman geworden. Ich plane dieses Buch meiner Frau und meinen Söhnen und deren Familien zu schenken. Darüber hinaus ist es aber auch geplant das Buch bei Veltaro zu veröffentlichen.
Aufgabenstellung
Auf dem Cover sollte neben meinem Namen Konrad(a) Pelzmann natürlich auch der Titel von dem Buch stehen. Ich habe dem Buch den Titel gegeben: 'Das Licht am Ufer'. Auf dem Backcover hatte ich mir eine kurze zusammenfassung vorgestellt, die ich auch beifüge. Ich hatte geplant, das sowohl auf dem Cover, wie auch auf dem Backcover Bilder von mir (u.a. als Baby) mit gestaltet werden. Aber das ist nur so eine Idee, ich bin da für Vorschläge offen
Das Design darf nicht zu überladen sein.

```html
<!DOCTYPE html>
<html lang="de">
<head>
<meta charset="utf-8">
<title>Das Licht am Ufer – Buchcover</title>
<link rel="stylesheet" href="https://fonts.googleapis.com/css2?family=Source+Serif+4:opsz,wght@8..60,400;8..60,500&display=swap">
<style>
  :root {
    --page-bg: #ffffff;
    --cover-tan: #e8b97f;
    --cover-edge: #d9a86e;
    --ink-navy: #272a44;
    --ink-body: #3a2f25;
    --frame-cream: #f2ece0;
    --frame-shadow: rgba(70, 45, 15, 0.28);
  }
  * { margin: 0; padding: 0; box-sizing: border-box; }
  html, body {
    width: 1200px; height: 955px; overflow: hidden;
    background: var(--page-bg);
  }
  .spread {
    position: absolute; left: 155px; top: 78px;
    display: flex; gap: 60px;
  }
  .cover {
    position: relative; width: 415px; height: 800px;
    background: var(--cover-tan);
    box-shadow: inset 0 0 0 1px var(--cover-edge);
    font-family: "Source Serif 4", Georgia, serif;
  }
  .snapshot {
    position: absolute; padding: 9px;
    background: var(--frame-cream);
    box-shadow: 0 3px 8px var(--frame-shadow);
  }
  .snapshot .photo { width: 100%; height: 100%; }
  .snap-baby    { left: 20px;  top: 35px;  width: 145px; height: 210px; transform: rotate(-3deg); }
  .snap-bike    { left: 185px; top: 65px;  width: 200px; height: 162px; transform: rotate(2deg); }
  .snap-youth   { left: 14px;  top: 258px; width: 138px; height: 214px; transform: rotate(-2deg); }
  .snap-frame   { left: 35px;  top: 482px; width: 196px; height: 158px; transform: rotate(-5deg); }
  .snap-toddler { left: 244px; top: 455px; width: 152px; height: 228px; transform: rotate(4deg); }

  .photo-baby    { background: linear-gradient(160deg, #d9cfc2, #b89a86 60%, #e4ddd3); }
  .photo-bike    { background: linear-gradient(180deg, #8c8577, #5e5c57 55%, #9a958c); }
  .photo-youth   { background: linear-gradient(170deg, #8a6f5c, #4f5d6c 55%, #6b6a66); }
  .photo-frame   { background: linear-gradient(120deg, #8ea1b0, #2d3138 55%, #5b6166); }
  .photo-toddler { background: linear-gradient(180deg, #6f7a55, #7f9aa8 50%, #8c8a5d); }

  .book-title {
    position: absolute; left: 170px; top: 272px;
    font-size: 56px; font-weight: 400; line-height: 1;
    color: var(--ink-navy); letter-spacing: -0.5px;
  }
  .book-title span { display: block; }
  .book-title .first { padding-left: 45px; }

  .author {
    position: absolute; left: 0; right: 0; top: 700px;
    text-align: center; font-size: 34px; font-weight: 400;
    color: var(--ink-navy);
  }

  .blurb {
    position: absolute; left: 32px; top: 78px; width: 315px;
    font-size: 12.5px; line-height: 1.35; color: var(--ink-body);
  }
  .blurb p { margin-bottom: 15px; }
  .back-portrait {
    position: absolute; left: 112px; top: 556px;
    width: 142px; height: 128px;
    background: linear-gradient(180deg, #b9c3c9, #8d9396 55%, #a9a59b);
  }
</style>
</head>
<body>
<main class="spread">
  <section class="cover cover-front">
    <figure class="snapshot snap-baby"><div class="photo photo-baby" role="img" aria-label="Babyfoto des Autors in hellem Pullover"></div></figure>
    <figure class="snapshot snap-bike"><div class="photo photo-bike" role="img" aria-label="Kind auf einem Fahrrad in einer Straße"></div></figure>
    <figure class="snapshot snap-youth"><div class="photo photo-youth" role="img" aria-label="Junger Mann im Jeanshemd vor einer Hauswand"></div></figure>
    <figure class="snapshot snap-frame"><div class="photo photo-frame" role="img" aria-label="Gerahmtes Familienfoto an einem Fenster"></div></figure>
    <figure class="snapshot snap-toddler"><div class="photo photo-toddler" role="img" aria-label="Kleinkind läuft über eine Wiese"></div></figure>
    <h1 class="book-title"><span class="first">Das</span><span>Licht</span><span>am Ufer</span></h1>
    <p class="author">Konrad(a) Pelzmann</p>
  </section>

  <section class="cover cover-back">
    <div class="blurb">
      <p>Ein Leben zwischen zwei Ufern, erzählt mit leiser Stimme und offenem Blick.</p>
      <p>Die Kindheit am Fluss, die ersten Wege mit dem Fahrrad, die Fragen nach Herkunft und Zugehörigkeit prägen diesen Roman von Anfang an.</p>
      <p>Später führen Arbeit, Liebe und Familie den Erzähler in neue Städte, doch die Erinnerung bleibt ein treuer Begleiter.</p>
      <p>Ein Buch für alle, die zurückschauen wollen.</p>
      <p>Was bleibt, wenn die Zeit vergeht? Welche Bilder tragen wir mit uns, und welche lassen wir los? Eine ehrliche Antwort auf diese Fragen sucht dieses Buch.</p>
      <p>Geschrieben für die eigene Familie und für jeden Leser, der in fremden Geschichten ein Stück der eigenen wiederfindet.</p>
    </div>
    <div class="back-portrait" role="img" aria-label="Porträt des Autors am Wasser"></div>
  </section>
</main>
</body>
</html>
```